Financial Advisor Brochure to attract new clients

I am launching a new career as a Financial Advisor and a flier that shows what services I offer and why I decided to go back to work at this point in my life. I have a deep desire to help people meet their dreams and believe that a solid financial foundation provides the ability to live your life as you want to and not how you have to. I created a simple flier but know that so much more can be done to catch a persons eye.

Target Market(s)

Entrepeneurs and Woman in all stages of life.

Industry/Entity Type

Financial Advisor

Font styles to use
Sans Serif

Colors
00AB8E
00BBA5
67D7C9
C6EFE9
E9F9F6

Requirements
Must have
• my photo, contact information and Cobaltra Logo

```html
<!DOCTYPE html>
<html lang="en">
<head>
<meta charset="utf-8">
<title>Cobaltra – Advisor Flyers</title>
<link href="https://fonts.googleapis.com/css2?family=Cinzel:wght@500;700&family=Montserrat:wght@400;500;800&display=swap" rel="stylesheet">
<style>
:root{
  --blue:#1d64ad;
  --ink:#222;
  --black:#0b0b0b;
  --white:#fff;
  --stage:#8b9294;
  --rule:#3a6fae;
  --phone-icon:#2f7fd0;
}
*{box-sizing:border-box;margin:0;padding:0}
html,body{width:1200px;height:3187px;overflow:hidden;background:var(--stage)}
body{position:relative;font-family:"Montserrat",Arial,sans-serif;color:var(--ink)}
.flyer{position:absolute;left:50px;width:1100px;height:1420px;background:var(--white);overflow:hidden;box-shadow:0 6px 18px rgba(0,0,0,.3)}
.flyer--profile{top:115px}
.flyer--services{top:1652px}
.abs{position:absolute}

/* profile */
.diagonal{left:0;top:0;width:1100px;height:1196px}
.brand{left:62px;top:78px;display:flex;align-items:center;gap:16px}
.brand__dot{width:54px;height:54px;border-radius:50%;background:var(--blue)}
.brand__name{font-family:"Cinzel",Georgia,serif;font-weight:500;font-size:46px;line-height:1;color:var(--ink)}
.advisor-name{left:58px;top:185px;font-family:"Cinzel",Georgia,serif;font-weight:700;font-size:116px;line-height:.98;color:var(--blue)}
.role{left:62px;top:425px;width:625px;border-top:2px solid var(--rule);border-bottom:2px solid var(--rule);padding:10px 0 8px;font-family:"Cinzel",Georgia,serif;font-size:38px;letter-spacing:13px;color:var(--ink)}
.tagline{left:62px;top:528px;width:528px;font-size:25px;line-height:1.3;color:var(--blue)}
.bio{left:62px;top:712px;width:490px;font-size:15.4px;line-height:1.3;text-align:justify}
.bio p{margin-bottom:19px}
.portrait{left:600px;top:500px;width:500px;height:696px}

.callbar{left:0;width:1100px;background:var(--black);display:flex;align-items:center;justify-content:space-between;color:var(--white)}
.callbar__label{font-size:31px}
.callbar__label b{font-weight:800}
.callbar__phone{display:flex;align-items:center;gap:18px;font-family:"Cinzel",Georgia,serif;font-size:66px;font-weight:500}
.contact{left:0;width:1100px;display:flex;justify-content:space-between;font-size:21px;font-weight:500;color:var(--ink)}

.flyer--profile .callbar{top:1196px;height:140px;padding:0 72px 0 68px}
.flyer--profile .contact{top:1366px;padding:0 72px 0 68px}

/* services */
.hero{left:0;top:0;width:1100px;height:538px}
.hero-title{left:80px;top:120px;font-family:"Cinzel",Georgia,serif;font-weight:700;font-size:66px;line-height:1.14;color:var(--white)}
.hero-rule{left:80px;top:445px;width:947px;height:2px;background:rgba(255,255,255,.7)}
.hero-photo{left:540px;top:34px;width:450px;height:504px}
.notch{left:100px;top:518px;width:40px;height:22px}

.service{width:440px}
.service__head{display:flex;align-items:center;gap:16px}
.service__icon{width:84px;height:84px;flex:none}
.service__title{font-family:"Cinzel",Georgia,serif;font-weight:500;font-size:30px;line-height:1.1;color:var(--blue)}
.service__note{font-size:17px;line-height:1.25;color:var(--ink);margin-top:2px}
.service ul{list-style:none;margin-top:18px}
.service li{position:relative;padding-left:22px;font-size:20px;line-height:1.3;margin-bottom:6px}
.service li::before{content:"";position:absolute;left:2px;top:5px;width:7px;height:13px;border:solid var(--blue);border-width:0 3px 3px 0;transform:rotate(40deg)}
.col-a{left:79px}
.col-b{left:605px}
.row-1{top:571px}
.row-2{top:840px}
.row-3{top:1126px}
.divider{height:2px;width:398px;background:var(--rule)}

.flyer--services .callbar{top:1250px;height:102px;padding:0 72px 0 80px}
.flyer--services .callbar__phone{font-size:60px}
.flyer--services .contact{top:1375px;padding:0 72px 0 80px}
</style>
</head>
<body>

<!-- Advisor profile flyer -->
<section class="flyer flyer--profile">
  <svg class="abs diagonal" viewBox="0 0 1100 1196" aria-hidden="true">
    <defs>
      <linearGradient id="panelBlue" x1="0" y1="0" x2="0" y2="1">
        <stop offset="0" stop-color="#1f62aa"/>
        <stop offset=".6" stop-color="#2a86d6"/>
        <stop offset="1" stop-color="#1d5ea6"/>
      </linearGradient>
    </defs>
    <polygon points="960,0 1100,0 1100,1196 700,1196" fill="url(#panelBlue)"/>
  </svg>

  <div class="abs brand">
    <span class="brand__dot"></span>
    <span class="brand__name">Cobaltra</span>
  </div>

  <h1 class="abs advisor-name">ROSALINDA<br>VERHOEF</h1>
  <div class="abs role">FINANCIAL ADVISOR</div>

  <p class="abs tagline">Passionate about helping empower you with knowledge to make informed financial decisions throughout all of life’s stages and help you achieve your goals.</p>

  <div class="abs bio">
    <p>As a business owner, wife, and mother of two teenagers, I understand the struggles you face juggling your personal, business, and financial life.</p>
    <p>I grew up in a home where my parents had opposing money habits. My Dad was a big spender and mom was a saver. Through the years, I saw how my mom’s consistent savings grew while Dad’s style led to many financial ups and downs. This made a huge impression on me and sparked my continued interest in all things finance.</p>
    <p>Having an entrepreneurial personality and ability to explain concepts in a relatable manner has provided me with many opportunities. In 2018, after decades of running a sales agency, I sold my company to spend time with my kids and family but my interest in Finance never waned. Now that our kids are thriving teenagers, I started a new career as a licensed Financial Advisor with a heart to help you achieve your financial dreams.</p>
    <p>The financial world is changing rapidly, and it can be confusing on how to maneuver through these times. My goal is to pull out the emotions that cloud judgement and help you make better decisions with your long-range goals in mind.</p>
  </div>

  <svg class="abs portrait" viewBox="0 0 500 696" role="img" aria-label="Portrait photo of the advisor, smiling, with long curly hair and a green blouse, against a blue backdrop">
    <defs>
      <linearGradient id="portraitTone" x1="0" y1="0" x2="0" y2="1">
        <stop offset="0" stop-color="#2f8fe0" stop-opacity="0"/>
        <stop offset=".15" stop-color="#8a6a4f" stop-opacity=".55"/>
        <stop offset=".55" stop-color="#1f8c84" stop-opacity=".75"/>
        <stop offset="1" stop-color="#137a70"/>
      </linearGradient>
    </defs>
    <rect x="0" y="0" width="500" height="696" fill="url(#portraitTone)"/>
  </svg>

  <div class="abs callbar">
    <span class="callbar__label"><b>CALL</b> FOR AN APPOINTMENT</span>
    <span class="callbar__phone">
      <svg width="40" height="40" viewBox="0 0 24 24" aria-hidden="true"><path fill="var(--phone-icon)" d="M6.6 10.8a15 15 0 0 0 6.6 6.6l2.2-2.2c.3-.3.7-.4 1-.2 1.1.4 2.3.6 3.6.6.6 0 1 .4 1 1V20c0 .6-.4 1-1 1A17 17 0 0 1 3 4c0-.6.4-1 1-1h3.5c.6 0 1 .4 1 1 0 1.2.2 2.4.6 3.6.1.3 0 .7-.2 1z"/></svg>
      407-555-0182
    </span>
  </div>
  <div class="abs contact">
    <span>rosa.verhoef@cobaltrawealth.com</span>
    <span>www.cobaltrawealth.com</span>
  </div>
</section>

<!-- Services flyer -->
<section class="flyer flyer--services">
  <svg class="abs hero" viewBox="0 0 1100 538" aria-hidden="true">
    <defs>
      <linearGradient id="heroBlue" x1="0" y1="0" x2="1" y2="0">
        <stop offset="0" stop-color="#1d62ab"/>
        <stop offset=".7" stop-color="#2a84d3"/>
        <stop offset="1" stop-color="#1f68b2"/>
      </linearGradient>
    </defs>
    <rect width="1100" height="538" fill="url(#heroBlue)"/>
  </svg>
  <h2 class="abs hero-title">Financial<br>Planning<br>Services<br>Offered</h2>
  <div class="abs hero-rule"></div>
  <svg class="abs hero-photo" viewBox="0 0 450 504" role="img" aria-label="Photo of the advisor resting her chin on her hand, curly hair, green blouse">
    <defs>
      <linearGradient id="heroPhotoTone" x1="0" y1="0" x2="0" y2="1">
        <stop offset="0" stop-color="#8a6a4f" stop-opacity=".35"/>
        <stop offset=".5" stop-color="#8a6a4f" stop-opacity=".6"/>
        <stop offset="1" stop-color="#168377"/>
      </linearGradient>
    </defs>
    <rect width="450" height="504" fill="url(#heroPhotoTone)"/>
  </svg>
  <svg class="abs notch" viewBox="0 0 40 22" aria-hidden="true"><polygon points="0,22 20,2 40,22" fill="#fff"/></svg>

  <!-- row 1 -->
  <div class="abs service col-a row-1">
    <div class="service__head">
      <svg class="service__icon" viewBox="0 0 84 84" aria-hidden="true"><circle cx="42" cy="42" r="40" fill="var(--blue)"/><circle cx="42" cy="42" r="33" fill="none" stroke="#fff" stroke-width="1.5" opacity=".6"/><path d="M28 52l22-22m-10 0h10v10M30 40a12 12 0 0 0 14 14" fill="none" stroke="#fff" stroke-width="3" stroke-linecap="round"/></svg>
      <h3 class="service__title">Transition<br>Planning</h3>
    </div>
    <ul><li>Divorce planning.</li><li>Strategy and guidance<br>pre, during, and post- divorce</li></ul>
  </div>
  <div class="abs service col-b row-1">
    <div class="service__head">
      <svg class="service__icon" viewBox="0 0 84 84" aria-hidden="true"><circle cx="42" cy="42" r="40" fill="var(--blue)"/><circle cx="42" cy="42" r="33" fill="none" stroke="#fff" stroke-width="1.5" opacity=".6"/><path d="M32 26v22h20v12M32 48l-4 12M52 48h6M36 36h10" fill="none" stroke="#fff" stroke-width="3" stroke-linecap="round"/><path d="M26 62q16 6 32 0" fill="none" stroke="#fff" stroke-width="3"/></svg>
      <h3 class="service__title">Retirement<br>Planning</h3>
    </div>
    <ul><li>Current portfolio analysis</li><li>Timeline asset and income planning</li><li>Tax and estate review and projections</li></ul>
  </div>
  <div class="abs divider col-a" style="top:806px"></div>
  <div class="abs divider col-b" style="top:806px"></div>

  <!-- row 2 -->
  <div class="abs service col-a row-2">
    <div class="service__head">
      <svg class="service__icon" viewBox="0 0 84 84" aria-hidden="true"><circle cx="42" cy="42" r="40" fill="var(--blue)"/><circle cx="42" cy="42" r="33" fill="none" stroke="#fff" stroke-width="1.5" opacity=".6"/><rect x="24" y="32" width="36" height="24" rx="2" fill="none" stroke="#fff" stroke-width="3"/><path d="M36 32v-5h12v5M24 42h36" fill="none" stroke="#fff" stroke-width="3"/></svg>
      <h3 class="service__title">Business Sale<br>or Purchase</h3>
    </div>
    <ul><li>Company valuations</li><li>Tax impact analysis</li><li>Strategy implementation for funds<br>received from sale</li></ul>
  </div>
  <div class="abs service col-b row-2">
    <div class="service__head">
      <svg class="service__icon" viewBox="0 0 84 84" aria-hidden="true"><circle cx="42" cy="42" r="40" fill="var(--blue)"/><circle cx="42" cy="42" r="33" fill="none" stroke="#fff" stroke-width="1.5" opacity=".6"/><path d="M26 42l16-14 16 14M31 38v14h22V38M24 58q8-6 18-2t18-2" fill="none" stroke="#fff" stroke-width="3" stroke-linejoin="round" stroke-linecap="round"/></svg>
      <h3 class="service__title">Real Estate<br>Acquisition or Sale</h3>
    </div>
    <ul><li>Acquisition or dissolution of real estate.<br>Individual or portfolio</li></ul>
  </div>
  <div class="abs divider col-a" style="top:1097px"></div>
  <div class="abs divider col-b" style="top:1097px"></div>

  <!-- row 3 -->
  <div class="abs service col-a row-3">
    <div class="service__head">
      <svg class="service__icon" viewBox="0 0 84 84" aria-hidden="true"><circle cx="42" cy="42" r="40" fill="var(--blue)"/><circle cx="42" cy="42" r="33" fill="none" stroke="#fff" stroke-width="1.5" opacity=".6"/><path d="M30 60V30h14v30M44 40h10v20M26 60h32M34 36h6M34 44h6M34 52h6M48 46h2M48 53h2" fill="none" stroke="#fff" stroke-width="3" stroke-linecap="round"/></svg>
      <div><h3 class="service__title">Estate Planning:</h3><p class="service__note">Strategies for creating<br>future generational wealth.</p></div>
    </div>
  </div>
  <div class="abs service col-b row-3">
    <div class="service__head">
      <svg class="service__icon" viewBox="0 0 84 84" aria-hidden="true"><circle cx="42" cy="42" r="40" fill="var(--blue)"/><circle cx="42" cy="42" r="33" fill="none" stroke="#fff" stroke-width="1.5" opacity=".6"/><circle cx="42" cy="34" r="10" fill="none" stroke="#fff" stroke-width="3"/><path d="M42 44v16M34 54q8-6 8 0M50 54q-8-6-8 0M30 60h24" fill="none" stroke="#fff" stroke-width="3" stroke-linecap="round"/><text x="42" y="39" text-anchor="middle" font-family="Montserrat,sans-serif" font-size="13" font-weight="800" fill="#fff">$</text></svg>
      <div><h3 class="service__title">New Investors:</h3><p class="service__note">Assistance in opening investment<br>and retirement acc</p></div>
    </div>
  </div>

  <div class="abs callbar">
    <span class="callbar__label"><b>CALL</b> FOR AN APPOINTMENT</span>
    <span class="callbar__phone">
      <svg width="36" height="36" viewBox="0 0 24 24" aria-hidden="true"><path fill="var(--phone-icon)" d="M6.6 10.8a15 15 0 0 0 6.6 6.6l2.2-2.2c.3-.3.7-.4 1-.2 1.1.4 2.3.6 3.6.6.6 0 1 .4 1 1V20c0 .6-.4 1-1 1A17 17 0 0 1 3 4c0-.6.4-1 1-1h3.5c.6 0 1 .4 1 1 0 1.2.2 2.4.6 3.6.1.3 0 .7-.2 1z"/></svg>
      407-555-0182
    </span>
  </div>
  <div class="abs contact">
    <span>rosa.verhoef@cobaltrawealth.com</span>
    <span>www.cobaltrawealth.com</span>
  </div>
</section>

</body>
</html>
```